Agricultural Consulting Website

Provide a modern yet business like website for my new Agriculture Consulting Business in Australia called FenTrove. Whilst we are based in Australia we are targetting both domestic and international markets (especially in Asia). We are targetting corporate, small business, government and farmer clients. The design should compliment our logo also sourced through pixel guild. The webiste should be easy for me to keep updated on a regular basis without the need to go back to the designer.

Industry/Entity Type

Business

Requirements
Must have
• clean crisp feel
• be modern yet business like
• be able to be updated by myself easily

```html
<!DOCTYPE html>
<html lang="en">
<head>
<meta charset="utf-8">
<title>FenTrove – Agricultural Consultants</title>
<link rel="stylesheet" href="https://fonts.googleapis.com/css2?family=Arimo:wght@400;700&family=Open+Sans:wght@400;600&display=swap">
<style>
  :root {
    --top-bar: #3d3d3d;
    --nav-bg: #232323;
    --nav-divider: #3a3a3a;
    --nav-text: #cfcfcf;
    --content-bg: #ecf0dc;
    --footer-bg: #cdd8a8;
    --brand-green: #6c9a1f;
    --brand-brown: #6b3a10;
    --button-green: #8db43c;
    --social-blue: #2b6fc8;
    --rule: #b9b9b9;
    --intro-text: #9b9b9b;
    --heading: #1f1f1f;
    --body-text: #333333;
    --white: #ffffff;
  }
  * { margin: 0; padding: 0; box-sizing: border-box; }
  html, body { width: 1200px; height: 900px; overflow: hidden; background: var(--white); }
  body { position: relative; font-family: "Arimo", Arial, sans-serif; color: var(--body-text); }

  .top-bar { position: absolute; left: 138px; top: 0; width: 942px; height: 20px; background: var(--top-bar); }
  .content-band { position: absolute; left: 138px; top: 277px; width: 942px; height: 566px; background: var(--content-bg); }

  .brand { position: absolute; left: 261px; top: 30px; display: flex; align-items: center; gap: 8px; }
  .brand-mark { width: 56px; height: 58px; background: var(--brand-brown); }
  .brand-name { font-family: "Open Sans", sans-serif; font-size: 38px; font-weight: 400; color: var(--brand-green); letter-spacing: -0.5px; }

  .social { position: absolute; top: 52px; left: 825px; display: flex; gap: 11px; list-style: none; }
  .social li { width: 24px; height: 24px; border-radius: 50%; background: var(--social-blue); box-shadow: 0 2px 3px rgba(0,0,0,.35); }

  .main-nav { position: absolute; left: 261px; top: 101px; width: 696px; height: 34px; background: var(--nav-bg); display: flex; list-style: none; }
  .main-nav li { height: 34px; line-height: 34px; font-size: 11px; color: var(--nav-text); text-align: center; border-right: 1px solid var(--nav-divider); }
  .main-nav li:last-child { border-right: none; }

  .hero { position: absolute; left: 261px; top: 135px; width: 696px; height: 238px; overflow: hidden;
          background: linear-gradient(180deg, #3f7fd6 0%, #8bb6e6 35%, #6d8c3e 70%, #2f4a1c 100%); }
  .hero-title { position: absolute; left: 17px; top: 10px; font-family: "Arimo", sans-serif; font-weight: 700; font-size: 42px; letter-spacing: 2px; color: var(--white); opacity: .92; }
  .hero-strip { position: absolute; left: 594px; top: 0; width: 60px; height: 238px; background: linear-gradient(180deg, #5aa53a, #8fd06a 60%, #4f9d34); }
  .hero-badge { position: absolute; left: 568px; top: 112px; width: 108px; height: 108px; border-radius: 50%; border: 2px solid #111;
                background: radial-gradient(circle at 50% 55%, #c9d9b4 0%, #eef2e6 70%, #ffffff 100%); }
  .hero-shadow { position: absolute; left: 285px; top: 373px; width: 648px; height: 18px; border-radius: 50%; background: radial-gradient(ellipse at center, rgba(0,0,0,.28), rgba(0,0,0,0) 70%); }

  .rule { position: absolute; left: 275px; width: 665px; height: 1px; background: var(--rule); }
  .rule.upper { top: 407px; }
  .rule.lower { top: 527px; }

  .intro { position: absolute; left: 230px; top: 424px; width: 755px; text-align: center; font-size: 20.5px; line-height: 28.5px; color: var(--intro-text); }

  .feature { position: absolute; top: 551px; width: 210px; }
  .feature h2 { font-size: 14.5px; font-weight: 400; color: var(--heading); height: 31px; white-space: nowrap; line-height: 20px; }
  .feature .frame { width: 203px; height: 96px; background: var(--white); padding: 7px; }
  .feature .photo { width: 100%; height: 82px; }
  .feature p, .feature ul { margin-top: 12px; font-size: 11px; line-height: 16.6px; color: var(--body-text); white-space: nowrap; }
  .feature ul { list-style: none; }
  .feature ul li { position: relative; padding-left: 17px; }
  .feature ul li svg { position: absolute; left: 0; top: 5px; }

  .feature.about { left: 263px; }
  .feature.about h2 { padding-left: 9px; }
  .feature.about p { padding-left: 1px; }
  .feature.services { left: 502px; }
  .feature.services h2 { padding-left: 2px; width: 260px; }
  .feature.services p { padding-left: 3px; }
  .feature.members { left: 753px; }
  .feature.members h2 { padding-left: 18px; width: 260px; }

  .photo.team { background: linear-gradient(180deg, #c9d3d6 0%, #8a8a86 40%, #4f8f2f 70%, #3f7a24 100%); }
  .photo.field { background: linear-gradient(180deg, #6a8f4a 0%, #b67a4c 30%, #a9623d 100%); }
  .photo.network { background: linear-gradient(180deg, #e6e8df, #b9bcb4 50%, #e2e4dc); }

  .button { position: absolute; height: 24px; line-height: 24px; background: var(--button-green); color: var(--white); font-size: 9px; text-align: center; letter-spacing: .3px; }
  .button.about-more { left: 397px; top: 797px; width: 50px; }
  .button.services-more { left: 641px; top: 797px; width: 50px; }
  .button.all-members { left: 843px; top: 797px; width: 107px; height: 25px; }

  .site-footer { position: absolute; left: 138px; top: 843px; width: 942px; height: 57px; background: var(--footer-bg); font-family: "Open Sans", sans-serif; }
  .copyright { position: absolute; left: 129px; top: 22px; font-size: 11px; color: #2a2a2a; }
  .footer-nav { position: absolute; right: 133px; top: 21px; display: flex; list-style: none; font-size: 9.5px; color: #2a2a2a; }
  .footer-nav li + li::before { content: "|"; margin: 0 6px; }
</style>
</head>
<body>
  <div class="top-bar"></div>
  <div class="content-band"></div>

  <header>
    <div class="brand">
      <span class="brand-mark"></span>
      <span class="brand-name">FenTrove</span>
    </div>
    <ul class="social" aria-label="Social links">
      <li></li><li></li><li></li><li></li>
    </ul>
    <nav>
      <ul class="main-nav">
        <li style="width:60px">Home</li>
        <li style="width:58px">About</li>
        <li style="width:65px">Product</li>
        <li style="width:68px">Services</li>
        <li style="width:60px">Clients</li>
        <li style="width:57px">Media</li>
        <li style="width:62px">Gallery</li>
        <li style="width:77px">Resources</li>
        <li style="width:69px">Careers</li>
        <li style="width:70px">Contact us</li>
      </ul>
    </nav>
  </header>

  <section class="hero" role="img" aria-label="Tall corn crop against a blue sky with a seedling in soil">
    <div class="hero-title">AGRICULTURE</div>
    <div class="hero-strip"></div>
    <div class="hero-badge" role="img" aria-label="Young seedling growing from a mound of soil"></div>
  </section>
  <div class="hero-shadow"></div>

  <div class="rule upper"></div>
  <p class="intro">The FenTrove Agricultural Consultants is the largest professional advisory<br>body in Australia supporting independent Agricultural Consultants<br>who provide advice to the agricultural industry</p>
  <div class="rule lower"></div>

  <section class="feature about">
    <h2>About FenTrove</h2>
    <div class="frame"><div class="photo team" role="img" aria-label="Group of consultants standing in a crop field"></div></div>
    <p>Lorem ipsum dolor sit amet, consectetur<br>adipiscing elit. Sed at ante. Mauris eleifend,<br>quam a vulputate dictum, massa quam<br>dapibus leo, eget vulputate orci purus ut<br>lorem. In fringilla mi in ligula.</p>
  </section>

  <section class="feature services">
    <h2>Services FenTrove Members Offer</h2>
    <div class="frame"><div class="photo field" role="img" aria-label="Tractor and advisers on a ploughed red soil field"></div></div>
    <p>Lorem ipsum dolor sit amet, consectetur<br>adipiscing elit. Sed at ante. Mauris eleifend,<br>quam a vulputate dictum, massa quam<br>dapibus leo, eget vulputate orci purus ut<br>lorem. In fringilla mi in ligula.</p>
  </section>

  <section class="feature members">
    <h2>Find a FenTrove Member</h2>
    <div class="frame"><div class="photo network" role="img" aria-label="Crowd of grey figures representing the member network"></div></div>
    <ul>
      <li><svg width="7" height="6" viewBox="0 0 7 6"><path d="M0 3h6M4 1l2 2-2 2" stroke="#555" fill="none"/></svg>400 qualified consultants</li>
      <li><svg width="7" height="6" viewBox="0 0 7 6"><path d="M0 3h6M4 1l2 2-2 2" stroke="#555" fill="none"/></svg>150 offices nationwide</li>
      <li><svg width="7" height="6" viewBox="0 0 7 6"><path d="M0 3h6M4 1l2 2-2 2" stroke="#555" fill="none"/></svg>Flexible hours</li>
      <li><svg width="7" height="6" viewBox="0 0 7 6"><path d="M0 3h6M4 1l2 2-2 2" stroke="#555" fill="none"/></svg>Provision of all in service packages</li>
      <li>Available to all farmers</li>
    </ul>
  </section>

  <a class="button about-more">MORE</a>
  <a class="button services-more">MORE</a>
  <a class="button all-members">ALL MEMBERS</a>

  <footer class="site-footer">
    <p class="copyright">@ 2013 FenTrove All Rights Reserved</p>
    <ul class="footer-nav">
      <li>Home</li><li>About</li><li>Product</li><li>Services</li><li>Clients</li><li>Gallery</li><li>Contact Us</li>
    </ul>
  </footer>
</body>
</html>
```